Dozevale 250 ml pouch design (190 x 120 mm) + logo.

Dozevale is a startup that focuses on one product: a powder supplement that intends to improve sleep quality (as opposed to melatonin products that focus on falling asleep). The target demographic is basically anyone with poor sleep but mostly adults (aged 30 - 45) who experience that bad sleep affects daily work performance.

The formula is a combination of glycine (3 g), magnesium bisglycinate (200 mg elemental), ashwagandha extract QRT-41 (300 mg), lemon balm extract (200 mg) and L-theanine (200 mg), and supporting ingredients inulin and natural cherry flavoring. Net weight will be approximately 180 - 190 grams with 30 servings.

For this product I seek a design for the pouch it comes in and the logo that accompanies it. For pouch reference, it is the 250 ml "Sturdy Sparrow" stand-up pouch from Wrapnelo.

Regarding pouch design, I'm thinking of the color blue with perhaps nuances of red or purple. Style should be relatively minimalist and convey trust. I would like to see some sort of ingredient stack on the front of the pouch to increase transparency and trust. The back of the pouch should leave room for the barcode, company details, regulatory claims (warnings), ingredient listing (again), allergy information, usage recommendation. These should be treated as text boxes that I can edit later.

The logo should of course mimic this style. One concrete idea that came to mind is to make some sort of stack icon (e.g. bars stacking) somewhere, perhaps in a letter S. This should represent the building of better quality sleep/ improving your sleep performance. Another angle could be the ingredient stack that helps achieve this. The stack icon could become the favicon/ textless logo.

The website is still in the making but will incorporate design elements of websites from Zorbly, Pebble vitals, Tiers vitals, Nine doze.

Font styles to use
Sans Serif

Colors
0054AA
0677BA
7BADD7
CADEEF
E8F1F8

```html
<!DOCTYPE html>
<html lang="en">
<head>
<meta charset="utf-8">
<title>Dozevale — Pouch &amp; Logo</title>
<link href="https://fonts.googleapis.com/css2?family=Montserrat:wght@400;500;600;700;800&display=swap" rel="stylesheet">
<style>
  :root{
    --brand-blue:#0054AA;
    --mid-blue:#0677BA;
    --sky:#7BADD7;
    --mist:#CADEEF;
    --ice:#E8F1F8;
    --navy:#0a1d66;
    --deep:#0c2a86;
    --accent:#3fe0f0;
    --stage:#efefef;
    --white:#ffffff;
  }
  *{margin:0;padding:0;box-sizing:border-box;}
  html,body{width:747px;height:1200px;overflow:hidden;}
  body{font-family:"Montserrat",sans-serif;background:var(--white);position:relative;}

  .logo-area{position:absolute;left:0;top:0;width:747px;height:274px;display:flex;align-items:center;justify-content:center;}
  .logo-wordmark{font-size:44px;font-weight:700;color:var(--brand-blue);letter-spacing:-0.5px;display:flex;align-items:center;gap:12px;}
  .logo-dot{width:16px;height:16px;background:var(--brand-blue);}

  .stage{position:absolute;left:0;top:274px;width:747px;height:926px;background:var(--stage);}

  .panel{position:absolute;overflow:hidden;color:var(--white);
    background:linear-gradient(180deg,var(--sky) 0%,#4f7fd0 28%,var(--deep) 62%,var(--navy) 100%);}
  .panel-back{left:55px;top:124px;width:313px;height:279px;}
  .panel-front{left:378px;top:124px;width:317px;height:279px;}
  .pouch-flat{left:210px;top:431px;width:330px;height:380px;}

  .panel-brand{position:absolute;left:14px;top:14px;font-size:9px;font-weight:700;color:var(--white);}

  /* back panel */
  .back-section{position:absolute;left:14px;width:140px;}
  .back-section h3{font-size:9px;font-weight:600;margin-bottom:3px;}
  .back-section p{font-size:5.5px;line-height:1.45;opacity:.9;}
  .sec-ingredients{top:36px;}
  .sec-use{top:98px;}
  .sec-warning{top:180px;}
  .barcode-space{position:absolute;left:14px;top:214px;width:46px;height:26px;}
  .company-details{position:absolute;left:14px;top:246px;font-size:5px;line-height:1.45;opacity:.85;}

  /* front panel */
  .ingredient-stack{position:absolute;right:14px;top:44px;text-align:right;font-size:5.5px;line-height:2.1;font-weight:500;}
  .ingredient-stack .servings{color:var(--accent);font-weight:600;margin-top:2px;}
  .moon-art{position:absolute;left:30px;top:62px;width:92px;height:140px;border-radius:6px;
    background:linear-gradient(180deg,rgba(232,241,248,.22),rgba(202,222,239,.08));}
  .front-title{position:absolute;left:14px;bottom:14px;font-size:26px;font-weight:700;line-height:1.05;letter-spacing:-0.3px;}
  .title-line{display:flex;align-items:center;gap:8px;}
  .badge{background:var(--accent);color:var(--navy);font-size:6px;font-weight:600;padding:2px 7px;border-radius:8px;letter-spacing:0;}

  .pouch-flat .panel-brand{left:18px;top:18px;font-size:10px;}
  .pouch-flat .ingredient-stack{right:18px;top:56px;font-size:6.5px;}
  .pouch-flat .moon-art{left:36px;top:84px;width:110px;height:160px;}
  .pouch-flat .front-title{left:18px;bottom:20px;font-size:31px;}
  .pouch-flat .badge{font-size:7px;}
</style>
</head>
<body>
  <header class="logo-area">
    <div class="logo-wordmark"><span class="logo-dot"></span>Dozevale</div>
  </header>

  <main class="stage">
    <section class="panel panel-back">
      <div class="panel-brand">Dozevale</div>
      <div class="back-section sec-ingredients">
        <h3>Ingredients</h3>
        <p>Glycine, magnesium bisglycinate, ashwagandha extract QRT-41, lemon balm extract, L-theanine, inulin, natural cherry flavouring.</p>
      </div>
      <div class="back-section sec-use">
        <h3>How To Use</h3>
        <p>Mix one scoop with 200 ml of water and drink 30 to 60 minutes before bed.</p>
      </div>
      <div class="back-section sec-warning">
        <h3>Warning</h3>
        <p>Do not exceed the daily dose. Not for pregnant women. Allergens: none.</p>
      </div>
      <div class="barcode-space"></div>
      <div class="company-details">Dozevale<br>Net weight 185 g<br>Keep dry, below 25°C</div>
    </section>

    <section class="panel panel-front">
      <div class="panel-brand">Dozevale</div>
      <div class="ingredient-stack">
        <div>Glycine (3 g)</div>
        <div>Magnesium Bisglycinate (200 mg)</div>
        <div>Ashwagandha Extract QRT-41 (300 mg)</div>
        <div>Lemon Balm Extract (200 mg)</div>
        <div>L-Theanine (200 mg)</div>
        <div class="servings">30 servings</div>
        <div>250 ml</div>
      </div>
      <div class="moon-art" role="img" aria-label="Crescent moon illustration"></div>
      <h1 class="front-title">
        <span class="title-line">Sleep <span class="badge">Better Sleep Quality</span></span>
        <span class="title-line">Supplement</span>
      </h1>
    </section>

    <section class="panel pouch-flat">
      <div class="panel-brand">Dozevale</div>
      <div class="ingredient-stack">
        <div>Glycine (3 g)</div>
        <div>Magnesium Bisglycinate (200 mg)</div>
        <div>Ashwagandha Extract QRT-41 (300 mg)</div>
        <div>Lemon Balm Extract (200 mg)</div>
        <div>L-Theanine (200 mg)</div>
        <div class="servings">30 servings</div>
        <div>250 ml</div>
      </div>
      <div class="moon-art" role="img" aria-label="Crescent moon illustration"></div>
      <h2 class="front-title">
        <span class="title-line">Sleep <span class="badge">Better Sleep Quality</span></span>
        <span class="title-line">Supplement</span>
      </h2>
    </section>
  </main>
</body>
</html>
```